Online Trading Web-Design

Web design is required for a new startup that specialises in online trading between buyers and sellers of fashion apparel. The company is called: Blue Harbor Commons (bhc)

Website needs to be clean and css friendly. we like the idea of having a largish "banner" on the homepage which we can rotate using HTML5. examples of the banners are: http://au.vextrano.com/ ; http://www.plorvak.com.au/

the logo has been established already, please limit designs around the colors already established (see uploaded logo).
Updates

Hi, a few clarifications:

1. although the website deals in online trading for clothes etc. the main focus of the website needs to be about highlighting trading between buyers (clothing stores) and sellers (clothing brands). so the website wont be directly selling items of clothes etc.

Industry/Entity Type

Fashion

```html
<!DOCTYPE html>
<html lang="en">
<head>
<meta charset="utf-8">
<title>Blue Harbor Commons</title>
<link href="https://fonts.googleapis.com/css2?family=Bebas+Neue&family=Noto+Serif:wght@400;700&family=Pacifico&display=swap" rel="stylesheet">
<style>
:root{
  --blue:#2a9cc8;
  --blue-dark:#1b7fa8;
  --orange:#d9651f;
  --orange-dark:#b9501a;
  --page:#d4eaf3;
  --hero:#dcf0f8;
  --white:#ffffff;
  --text:#555a5e;
  --muted:#8a9094;
  --line:#d2d7da;
  --dark:#343434;
  --cream:#fcf8e8;
}
*{box-sizing:border-box;margin:0;padding:0}
html,body{width:1200px;height:2540px;overflow:hidden}
body{background:var(--page);font-family:"Noto Serif",serif;color:var(--text);position:relative}
.abs{position:absolute}
.head{font-family:"Bebas Neue",sans-serif;letter-spacing:.5px}
a{color:inherit;text-decoration:none}

/* header */
.admin-tab{left:1111px;top:0;width:70px;height:25px;background:#3a3a3a;color:#eee;font:10px "Noto Serif",serif;text-align:center;line-height:25px}
.header{left:25px;top:25px;width:1150px;height:144px;background:var(--white)}
.logo{left:42px;top:48px;display:flex;align-items:center;gap:14px}
.logo-mark{width:40px;height:40px;border-radius:50%;background:var(--blue)}
.logo-name{font-family:"Noto Serif",serif;font-size:24px;color:var(--blue);font-weight:700}
.toplinks{left:520px;top:50px;font-size:14px;color:var(--text);white-space:nowrap}
.toplinks a{padding:0 10px;border-right:1px solid #aaa}
.toplinks a:last-child{border:0}
.toplinks .on{color:var(--blue)}
.phone-pill{left:898px;top:42px;width:266px;height:36px;border-radius:18px;background:#e6f4fa;display:flex;align-items:center;gap:8px;padding-left:12px;color:var(--blue-dark);font-size:19px;white-space:nowrap;line-height:1}
.search{left:847px;top:100px;width:313px;height:40px;border:1px solid var(--line);background:#fff;font-size:15px;color:#999;padding:9px 8px}
.search-btn{left:1120px;top:102px;width:38px;height:36px;background:var(--blue)}

/* nav */
.nav{left:25px;top:169px;width:1150px;height:55px;background:#ecf6fb;border-bottom:2px solid #c5e2ee;display:flex}
.nav a{font-family:"Bebas Neue",sans-serif;font-size:29px;color:var(--blue-dark);padding:12px 22px 0;height:55px}
.nav a.on{background:var(--blue);color:#fff}

/* hero */
.hero{left:25px;top:224px;width:1150px;height:420px;background:var(--hero)}
.hero-copy{left:131px;top:285px;width:545px;display:flex;flex-direction:column;align-items:flex-start}
.hero-title{font-size:54px;line-height:60px;color:var(--blue-dark);font-weight:400}
.hero-text{margin-top:20px;font-size:14px;line-height:26px;color:#4b4f52;text-align:justify}
.btn-more{margin-top:14px;width:108px;height:34px;border:1px solid #a8cfe0;background:#fff;color:var(--blue-dark);font-size:17px;text-align:center;line-height:32px;border-radius:3px}
.hero-photo{left:815px;top:235px;width:290px;height:335px;border-radius:40px 40px 26px 26px;background:radial-gradient(circle at 45% 45%,#f5c545,#e59d1a 70%,#c67f12)}
.dots{left:502px;top:612px;display:flex;gap:9px}
.dots i{width:12px;height:12px;border-radius:50%;background:#555}
.dots i.on{background:var(--blue)}

/* deals */
.deals{left:25px;top:677px;width:1150px;height:449px;background:#fff;box-shadow:0 2px 6px rgba(0,0,0,.12)}
.ribbon{left:360px;top:656px;width:482px;height:44px;background:var(--blue);color:#fff;text-align:center;font-size:32px;line-height:46px;clip-path:polygon(0 50%,4% 0,96% 0,100% 50%,96% 100%,4% 100%)}
.deal{top:730px;width:250px}
.deal .cat{font-size:14px;color:#333}
.deal h3{font-family:"Bebas Neue",sans-serif;font-size:31px;color:var(--orange);font-weight:400;margin-top:6px}
.deal .ph{width:248px;height:190px;border:1px solid var(--line);margin-top:8px}
.deal p{font-size:14px;line-height:24px;margin-top:14px;color:#555}
.deal .more{display:block;text-align:right;color:var(--blue-dark);font-size:14px;margin-top:22px}

/* main body */
.main{left:25px;top:1153px;width:1150px;height:900px;background:#fff}
.side-ribbon{height:50px;background:var(--blue);color:#fff;font-size:32px;padding:8px 0 0 12px;clip-path:polygon(0 0,94% 0,100% 50%,94% 100%,0 100%)}
.menu a{display:block;font-size:15px;color:#333;border-bottom:1px dotted #b9c0c4;padding:10px 0 10px 16px}
.menu a.on{color:var(--blue-dark);font-weight:700}
.sec-title{font-size:30px;color:var(--orange);white-space:nowrap}
.dotline{border-bottom:3px dotted #c7ccd0}
.feed{left:38px;top:1520px;width:275px;height:487px;background:var(--cream);border:1px solid #e3d7a8;border-radius:6px;padding:16px 12px;font-size:13.5px;line-height:28px;color:#333}
.feed b{color:var(--blue-dark)}
.feed .meta{color:var(--muted);font-size:13px}
.feed .tw{margin-bottom:18px}
.art-title{font-family:"Bebas Neue",sans-serif;font-size:26px;color:var(--orange);font-weight:400;white-space:nowrap}
.art-img{width:182px;height:192px;border:1px solid var(--line)}
.art-text{width:316px;font-size:15px;line-height:33px;text-align:justify;color:#444}
.btn-blue{width:103px;height:32px;border-radius:5px;background:var(--blue);color:#fff;font-size:15px;text-align:center;line-height:32px}
.delivery{left:889px;top:1185px;width:288px;height:187px;background:var(--blue);color:#fff}
.blog p{font-size:14px;line-height:24px;color:#444}
.blog .meta{font-size:14px;color:#444;display:flex;gap:14px;align-items:center;margin:8px 0 14px;padding-bottom:12px;border-bottom:2px dotted #c7ccd0}
.blog .meta span{display:flex;gap:5px;align-items:center}

/* footer */
.contact{left:30px;top:2085px;width:279px;height:279px;border-radius:50%;background:var(--orange);border:6px solid #fff;box-shadow:0 0 0 4px var(--orange-dark);color:#fff;text-align:center}
.foot-links a{display:block;font-size:15px;color:#333;padding:10px 0 10px 20px;border-bottom:1px dotted #b9c0c4;position:relative}
.foot-links a::before{content:"»";position:absolute;left:2px;color:#333}
.footer-bar{left:0;top:2424px;width:1200px;height:116px;background:var(--dark)}
</style>
</head>
<body>

<div class="abs admin-tab">ADMIN</div>

<header class="abs header"></header>
<div class="abs logo"><span class="logo-mark"></span><span class="logo-name">Blue Harbor Commons</span></div>
<nav class="abs toplinks"><a class="on">Home</a><a>About us</a><a>Log in</a><a>Create an account</a></nav>
<div class="abs phone-pill head">
  <svg width="20" height="20" viewBox="0 0 24 24"><path fill="#1b7fa8" d="M6.6 10.8a15 15 0 0 0 6.6 6.6l2.2-2.2c.3-.3.7-.4 1-.2 1.1.4 2.3.6 3.6.6.6 0 1 .4 1 1V20c0 .6-.4 1-1 1A17 17 0 0 1 3 4c0-.6.4-1 1-1h3.5c.6 0 1 .4 1 1 0 1.3.2 2.5.6 3.6.1.3 0 .7-.2 1z"/></svg>
  <span>800 55501234 &nbsp;ONLINE SUPPORT</span>
</div>
<div class="abs search">Enter your keywords</div>
<div class="abs search-btn"><svg width="38" height="36" viewBox="0 0 38 36"><path d="M13 11l7 7-7 7M20 11l7 7-7 7" stroke="#fff" stroke-width="3" fill="none"/></svg></div>

<nav class="abs nav"><a class="on">Home</a><a>Typography</a><a>Template Features</a><a>Q7 Showcase</a><a>Demo Content</a></nav>

<section class="abs hero"></section>
<div class="abs hero-copy">
  <h1 class="hero-title head">Trailpack Antics Seri...</h1>
  <p class="hero-text">Suspendisse potenti. Nullam felis purus, scelerisque quis adipiscing sed, malesuada quis enim. Nullam dapibus consequat imperdiet. Proin at tincidunt urna. Etiam non urna vel diam sollicitudin fringilla vitae a risus. Praesent euismod, ipsum eu ultrices auctor, turpis turpis mollis leo, id tincidu...</p>
  <a class="btn-more">Read more</a>
</div>
<div class="abs hero-photo" role="img" aria-label="Photo of a yellow leather handbag"></div>
<svg class="abs" style="left:46px;top:435px" width="26" height="36"><path d="M20 4L6 18l14 14" stroke="#fff" stroke-width="5" fill="none"/></svg>
<svg class="abs" style="left:1128px;top:435px" width="26" height="36"><path d="M6 4l14 14L6 32" stroke="#fff" stroke-width="5" fill="none"/></svg>
<div class="abs dots"><i class="on"></i><i></i><i></i><i></i><i></i><i></i><i></i><i></i><i></i><i></i></div>

<section class="abs deals"></section>
<div class="abs ribbon head">« • • • • &nbsp; Deals of the Day &nbsp; • • • • »</div>

<article class="abs deal" style="left:42px"><div class="cat">Handbags »</div><h3>Leather Ashlee Tote...</h3><div class="ph" role="img" aria-label="Photo of a black and white tote bag" style="background:linear-gradient(#f4f4f4,#d8dbde)"></div><p>Consequat in arcu ipsum nunc cursus felis et...</p><a class="more">Read more »</a></article>
<article class="abs deal" style="left:328px"><div class="cat">Handbags »</div><h3>Leather Ashlee Tote...</h3><div class="ph" role="img" aria-label="Photo of a black and white tote bag" style="background:linear-gradient(#f4f4f4,#d8dbde)"></div><p>Consequat in arcu ipsum nunc cursus felis et...</p><a class="more">Read more »</a></article>
<article class="abs deal" style="left:614px"><div class="cat">Handbags »</div><h3>Nulla Adipiscing...</h3><div class="ph" role="img" aria-label="Photo of a pink leather handbag" style="background:linear-gradient(#f7eef0,#d9a3ae)"></div><p>Urna Mauris convallis id orci orci sodales Nam...</p><a class="more">Read more »</a></article>
<article class="abs deal" style="left:900px"><div class="cat">Handbags »</div><h3>Quisque Scelerisque...</h3><div class="ph" role="img" aria-label="Photo of a beige printed tote bag" style="background:linear-gradient(#f6f3ee,#dccfb8)"></div><p>Consequat in arcu ipsum nunc cursus felis et...</p><a class="more">Read more »</a></article>

<section class="abs main"></section>

<!-- left column -->
<div class="abs side-ribbon head" style="left:21px;top:1185px;width:292px">Main Menu &nbsp;• • • • »</div>
<nav class="abs menu" style="left:21px;top:1240px;width:292px"><a class="on">HOME</a><a>TYPOGRAPHY</a><a>TEMPLATE FEATURES</a><a>Q7 SHOWCASE</a><a>DEMO CONTENT</a></nav>
<div class="abs sec-title head" style="left:38px;top:1475px">KW Social Feeds <span style="color:#c7ccd0">• • • •</span></div>
<span class="abs" style="left:284px;top:1478px;width:28px;height:28px;border-radius:50%;background:var(--blue)"></span>
<div class="abs feed">
  <div class="tw"><b>Knotworks</b> KW Slideshow Pro version 1.1 has been upgraded. 5 Amazing slideshow template added! Try it now! <b>kw.link/4t7Qp2</b><div class="meta">20 minutes ago · reply · retweet · favorite</div></div>
  <div class="tw"><b>Knotworks</b> Amazing photographer template for Cmsly 2.5. Preview and comment now! <b>kw.link/9m3Rx8</b><div class="meta">4 days ago · reply · retweet · favorite</div></div>
  <div class="tw"><b>Knotworks</b> Amazing photographer template for Cmsly 2.5.Preview and comment!<div class="meta">4 days ago · reply · retweet · favorite</div></div>
</div>

<!-- center column -->
<div class="abs sec-title head" style="left:341px;top:1185px">Frontpage Content</div>
<div class="abs dotline" style="left:548px;top:1200px;width:316px"></div>
<h2 class="abs art-title" style="left:341px;top:1228px">Vestibulum faucibus, leo in pulvinar iaculis 2</h2>
<div class="abs art-img" style="left:343px;top:1270px;background:linear-gradient(135deg,#f2f2f2,#d98a8c)" role="img" aria-label="Photo of a woman wearing a headset"></div>
<p class="abs art-text" style="left:542px;top:1262px">Lorem ipsum dolor sit amet, consectetur adipiscing elit. Etiam et neque, placerat a congue vel, luctus non lacus. Morbi rhoncus lectus lectus luctus aliquet. Ut suscipit malesuada blandit. Integer sodales arcu nec enim semper lacinia</p>
<a class="abs btn-blue" style="left:754px;top:1492px">Read more</a>
<div class="abs dotline" style="left:341px;top:1540px;width:523px"></div>
<h2 class="abs art-title" style="left:341px;top:1568px">Class aptent taciti sociosqu ad litora torquent 1</h2>
<div class="abs art-img" style="left:343px;top:1613px;background:linear-gradient(135deg,#f4f4f4,#b9b9b9)" role="img" aria-label="Photo of a woman in a light coat"></div>
<p class="abs art-text" style="left:542px;top:1605px">Lorem ipsum dolor sit amet, consectetur adipiscing elit. Etiam et neque, placerat a congue vel, luctus non lacus. Morbi rhoncus lectus lectus luctus aliquet. Ut suscipit malesuada blandit. Integer sodales arcu nec enim semper lacinia</p>
<a class="abs btn-blue" style="left:754px;top:1834px">Read more</a>
<div class="abs dotline" style="left:341px;top:1885px;width:523px"></div>

<!-- right column -->
<div class="abs delivery">
  <svg class="abs" style="left:16px;top:16px" width="62" height="62" viewBox="0 0 62 62"><rect width="62" height="62" rx="8" fill="#1b7fa8"/><rect x="10" y="16" width="28" height="22" rx="3" fill="#fff"/><path d="M38 22h9l6 8v8H38z" fill="#fff"/><circle cx="20" cy="42" r="5" fill="#fff" stroke="#1b7fa8" stroke-width="2"/><circle cx="46" cy="42" r="5" fill="#fff" stroke="#1b7fa8" stroke-width="2"/></svg>
  <div class="abs head" style="left:94px;top:14px;font-size:34px">Free Delivery</div>
  <div class="abs" style="left:94px;top:52px;font-size:18px;font-style:italic">within 50 miles</div>
  <div class="abs head" style="left:18px;top:120px;width:252px;height:44px;background:#1b6f93;font-size:32px;text-align:center;line-height:46px;clip-path:polygon(0 50%,6% 0,94% 0,100% 50%,94% 100%,6% 100%)">«« More Info »»</div>
</div>
<div class="abs sec-title head" style="left:893px;top:1400px">Our Blog</div>
<div class="abs dotline" style="left:990px;top:1418px;width:140px"></div>
<div class="abs" style="left:1132px;top:1398px;width:45px;height:45px;background:var(--orange);clip-path:polygon(0 0,100% 0,100% 100%)"></div>
<div class="abs blog" style="left:893px;top:1450px;width:258px">
  <p>Aenean ut lacus non velit porta adipiscing.</p>
  <div class="meta"><span><svg width="18" height="18"><circle cx="9" cy="9" r="7" stroke="#444" stroke-width="2" fill="none"/><path d="M9 5v4h3" stroke="#444" stroke-width="2" fill="none"/></svg>20/12/2011</span><span>▤ 16 comments</span></div>
  <p>Praesent ultricies lacus non eros ullamcorper suscipit</p>
  <div class="meta"><span><svg width="18" height="18"><circle cx="9" cy="9" r="7" stroke="#444" stroke-width="2" fill="none"/><path d="M9 5v4h3" stroke="#444" stroke-width="2" fill="none"/></svg>20/12/2011</span><span>▤ 6 comments</span></div>
  <p>Fusce interdum orci eget nulla tincidunt at commodo</p>
  <div class="meta"><span><svg width="18" height="18"><circle cx="9" cy="9" r="7" stroke="#444" stroke-width="2" fill="none"/><path d="M9 5v4h3" stroke="#444" stroke-width="2" fill="none"/></svg>20/12/2011</span><span>▤ 3 comments</span></div>
  <p>Class aptent taciti sociosqu ad litora torquent 2</p>
  <div class="meta"><span><svg width="18" height="18"><circle cx="9" cy="9" r="7" stroke="#444" stroke-width="2" fill="none"/><path d="M9 5v4h3" stroke="#444" stroke-width="2" fill="none"/></svg>17/11/2011</span><span>▤ 6 comments</span></div>
  <p>Class aptent taciti sociosqu ad litora torquent</p>
  <div class="meta"><span><svg width="18" height="18"><circle cx="9" cy="9" r="7" stroke="#444" stroke-width="2" fill="none"/><path d="M9 5v4h3" stroke="#444" stroke-width="2" fill="none"/></svg>17/11/2011</span><span>▤ 19183 comments</span></div>
</div>

<svg class="abs" style="left:581px;top:2035px" width="38" height="38"><circle cx="19" cy="19" r="17" fill="#e9ecee" stroke="#c7ccd0" stroke-width="2"/><path d="M12 22l7-7 7 7M12 28l7-7 7 7" stroke="#888" stroke-width="2.5" fill="none"/></svg>

<!-- footer -->
<div class="abs contact">
  <div style="font-family:'Pacifico',cursive;font-size:38px;margin-top:22px">Contact us</div>
  <div class="head" style="font-size:50px;margin-top:4px">800 5550 1234</div>
  <div style="font-size:13px;line-height:20px;margin-top:2px">12 Harbor Row - Dock Ward -<br>Port Vale</div>
  <div style="display:flex;gap:14px;justify-content:center;margin-top:10px"><span style="width:34px;height:34px;border-radius:50%;background:#3a2a1f"></span><span style="width:34px;height:34px;border-radius:50%;background:#3a2a1f"></span><span style="width:34px;height:34px;border-radius:50%;background:#3a2a1f"></span></div>
</div>
<div class="abs sec-title head" style="left:330px;top:2096px">Our Product <span style="color:#c7ccd0">• • • • • • • •</span></div>
<nav class="abs foot-links" style="left:330px;top:2138px;width:248px"><a>Handbags</a><a>Tote bags</a><a>Carpet bags</a><a>Laptop bags</a><a>Handbags</a><a>Tote bags</a></nav>
<div class="abs sec-title head" style="left:616px;top:2096px">About us <span style="color:#c7ccd0">• • • • • • • • •</span></div>
<nav class="abs foot-links" style="left:616px;top:2138px;width:252px"><a>About us</a><a>Forum support</a><a>Privacy Policy</a><a>Customer Service</a><a>Contact us</a><a>Site Map</a></nav>
<div class="abs sec-title head" style="left:898px;top:2096px">Our Brand <span style="color:#c7ccd0">• • • • • • • • •</span></div>
<div class="abs" style="left:900px;top:2140px;width:232px;height:135px;background:radial-gradient(ellipse at center,#b9bec2,#e4e7e9 70%)" role="img" aria-label="World map with location pins"></div>
<div class="abs" style="left:898px;top:2280px;width:264px;height:101px;background:var(--blue);color:#fff;font-size:14px;line-height:24px;padding:10px 8px;border-radius:4px">Duis nunc metus egestas Quisque facilisi cursus penatibus dis eros rutrum</div>

<footer class="abs footer-bar"></footer>
</body>
</html>
```